Business card and (possibly) logo

Hi - we need a new business card.
We have an existing logo that we quite like but we are open to options.
We are an architectural firm - we specialize in upmarket residential work and apartment blocks.
We are chasing a business card at present but also want to extensively update our website going forward to attract a much higher level of client / investor / developer.
Our current logo is black, grey and yellow and based on the sun/moon temples in Mexico.
We are open to variations.
We want to communicate professionalism, trust, quality.
Our website is www.korvalstudio.com.au - but note as above - we want to change the website as well to be a lot 'classier' and to appeal to a higher end market.

thanks

Target Market(s)

We are an architect firm - our target market is Developers and builders of high end houses and luxury apartment blocks. Also private home owners wanting to build excellent expensive houses. (ideally over $1m budgets)

Industry/Entity Type

Residential

Requirements
Must have
• Logo
Contact details;
Name
phone, mobile, email, web

```html
<!DOCTYPE html>
<html lang="en">
<head>
<meta charset="utf-8">
<title>Korval Studio — Business Card</title>
<link rel="stylesheet" href="https://fonts.googleapis.com/css2?family=Open+Sans:wght@300;400&display=swap">
<style>
  :root {
    --page-bg: #e9e6e1;
    --card-black: #000000;
    --text-white: #ffffff;
    --text-soft: #e6e6e6;
    --accent-yellow: #f0d85a;
    --accent-olive: #8c8f4e;
    --accent-red: #d8553f;
  }
  * { margin: 0; padding: 0; box-sizing: border-box; }
  html, body {
    width: 1200px;
    height: 900px;
    overflow: hidden;
    background: var(--page-bg);
    font-family: "Open Sans", "Segoe UI", sans-serif;
  }
  .canvas {
    position: relative;
    width: 1200px;
    height: 900px;
  }
  .card {
    position: absolute;
    width: 540px;
    height: 330px;
    background: var(--card-black);
    color: var(--text-white);
    box-shadow: 0 6px 18px rgba(0, 0, 0, 0.25);
  }
  .card--front { left: 580px; top: 90px; }
  .card--back  { left: 80px;  top: 480px; }

  /* Front: wordmark */
  .wordmark {
    position: absolute;
    left: 50%;
    top: 50%;
    transform: translate(-50%, -50%);
    display: flex;
    align-items: center;
    gap: 14px;
  }
  .wordmark__name {
    font-weight: 300;
    color: var(--text-white);
    text-align: center;
    line-height: 1;
  }
  .wordmark__primary {
    display: block;
    font-size: 58px;
    letter-spacing: 2px;
  }
  .wordmark__secondary {
    display: block;
    font-size: 17px;
    letter-spacing: 12px;
    margin-top: 4px;
    margin-right: -12px;
  }
  .wordmark__square {
    width: 16px;
    height: 16px;
    background: var(--accent-yellow);
  }

  /* Back: person and contact */
  .person {
    position: absolute;
    left: 0;
    right: 0;
    top: 62px;
    text-align: center;
  }
  .person__name {
    font-size: 22px;
    font-weight: 400;
    line-height: 1.1;
  }
  .person__role {
    font-size: 12px;
    font-weight: 300;
    color: var(--text-soft);
  }
  .contact {
    position: absolute;
    left: 26px;
    bottom: 30px;
    font-size: 14px;
    font-weight: 300;
    line-height: 1.22;
    color: var(--text-soft);
    font-style: normal;
  }
  .edge-pattern {
    position: absolute;
    right: 0;
    top: 0;
    width: 46px;
    height: 100%;
    display: block;
  }
</style>
</head>
<body>
  <main class="canvas">
    <section class="card card--front" aria-label="Card front">
      <div class="wordmark">
        <div class="wordmark__name">
          <span class="wordmark__primary">KORVAL</span>
          <span class="wordmark__secondary">STUDIO</span>
        </div>
        <span class="wordmark__square" aria-hidden="true"></span>
      </div>
    </section>

    <section class="card card--back" aria-label="Card back">
      <div class="person">
        <p class="person__name">Lena Varsh</p>
        <p class="person__role">architect</p>
      </div>
      <address class="contact">
        Suite 8, 42 - 48 Marlow Coast Road<br>
        Marlow WA 6021<br>
        1300 72 18 54<br>
        lenavarsh@korvalst.com<br>
        www.korvalstudio.com.au
      </address>
      <svg class="edge-pattern" viewBox="0 0 46 330" preserveAspectRatio="none" role="img" aria-label="Stepped zigzag border ornament in yellow, olive and red">
        <defs>
          <linearGradient id="edgeTones" x1="0" y1="0" x2="1" y2="0">
            <stop offset="0" stop-color="var(--accent-olive)"/>
            <stop offset="0.55" stop-color="var(--accent-yellow)"/>
            <stop offset="1" stop-color="var(--accent-red)"/>
          </linearGradient>
        </defs>
        <rect x="0" y="0" width="46" height="330" fill="url(#edgeTones)"/>
      </svg>
    </section>
  </main>
</body>
</html>
```